Marcus Delwyn-Hart Finance

Need a personal website advertising Equipment Finance,Business Finance,Commercial Finance, Construction Finance, Bridging Finance. Similar websites are www.qorvimark.com.au / www.talsbrio.com.au / www.zpk7.com.au /wwwlemberwick.com.au

Target Market(s)

Business People

Industry/Entity Type

Business

Number of Pages Required

3 page

Font styles to use
Serif
Sans Serif

Requirements
Must have
• All i want is a simple corporate looking website advertising Equipment Finance, Commercial Finance, Construction Finance, Business Finance, Bridging Finance,

```html
<!DOCTYPE html>
<html lang="en">
<head>
<meta charset="utf-8">
<title>Marcus Delwyn-Hart Finance</title>
<link href="https://fonts.googleapis.com/css2?family=Lato:wght@400;700&family=Open+Sans:wght@600;700&display=swap" rel="stylesheet">
<style>
:root{
  --blue:#2e5ca8;
  --blue-dark:#1e3f8f;
  --ink:#111;
  --text:#222;
  --light:#f5f5f5;
  --panel:#ebebeb;
  --line:#d6d6d6;
  --white:#fff;
  --black:#000;
}
*{box-sizing:border-box;margin:0;padding:0}
html,body{width:884px;height:1200px;overflow:hidden;background:var(--white)}
body{position:relative;font-family:'Lato',sans-serif;color:var(--text)}
.abs{position:absolute}
.head-font{font-family:'Open Sans',sans-serif}

/* header */
.site-header{left:0;top:0;width:884px;height:70px;background:var(--light)}
.brand{left:73px;top:12px;display:flex;align-items:center;gap:10px}
.brand-mark{width:44px;height:44px;background:var(--blue)}
.brand-name{font-family:'Open Sans',sans-serif;font-weight:600;font-size:19px;color:var(--blue)}
.main-nav{left:407px;top:33px;display:flex;gap:25px;font-size:10.5px;font-weight:700;color:#222;letter-spacing:.2px}
.main-nav .active{color:var(--blue);position:relative}
.main-nav .active::after{content:"";position:absolute;left:0;right:0;top:32px;height:2px;background:var(--blue)}
.call{left:700px;top:20px;display:flex;align-items:center;gap:8px}
.call-divider{width:1px;height:30px;background:#333}
.call-text{font-size:10.5px;font-weight:700;line-height:15px}
.call-text span{display:block;color:var(--blue)}

/* hero */
.hero{left:0;top:70px;width:884px;height:380px;background:linear-gradient(160deg,#9fbde0 0%,#cfdcea 45%,#8a96a4 80%,#6a737c 100%)}
.hero-caption{left:0;top:208px;width:414px;height:108px;background:rgba(255,255,255,.55)}
.hero-title{left:72px;top:220px;font-size:27px;font-weight:600;color:var(--ink)}
.hero-lead{left:73px;top:258px;width:330px;font-size:11px;line-height:15px;color:#111}
.btn{background:var(--blue);color:var(--white);font-size:11px;font-weight:700;display:flex;align-items:center;justify-content:center}
.hero-btn{left:73px;top:305px;width:103px;height:26px;border:1px solid #fff}
.dots{left:73px;top:356px;display:flex;gap:4px}
.dots i{width:8px;height:8px;border:1px solid var(--blue)}
.dots i:first-child{background:var(--blue)}

/* welcome */
.welcome-title{left:72px;top:497px;font-size:22px;font-weight:700;color:var(--ink)}
.welcome-title span{color:var(--blue)}
.rule{height:2px;background:var(--blue)}
.welcome-rule{left:72px;top:536px;width:49px}
.welcome-text{left:74px;top:558px;width:510px;font-size:10.3px;line-height:16px;color:#111}
.read-btn{left:73px;top:657px;width:89px;height:27px}

/* inquiry */
.inquiry{left:611px;top:487px;width:202px;height:207px;background:var(--panel);box-shadow:0 6px 6px -4px rgba(0,0,0,.35)}
.inquiry-title{left:0;top:10px;width:202px;text-align:center;font-size:16px;font-weight:700;color:var(--ink)}
.inquiry-title span{color:var(--blue)}
.field{left:13px;width:176px;background:var(--white);border:1px solid var(--line);font-size:8.5px;color:#666;padding:8px 7px}
.submit{left:13px;top:169px;width:176px;height:28px;font-size:12px}

/* services */
.services-band{left:0;top:726px;width:884px;height:135px;background:linear-gradient(120deg,#1a4bb0 0%,#1c53b8 40%,#1f62b4 65%,#138b9c 100%)}
.services-title{left:0;top:746px;width:884px;text-align:center;color:var(--white);font-size:23px;font-weight:700}
.services-rule{left:418px;top:788px;width:48px;background:#cfd6e4}
.service{top:820px;width:130px;display:flex;flex-direction:column;align-items:center}
.service-box{width:76px;height:76px;background:var(--white);border:2px solid var(--blue);display:flex;align-items:center;justify-content:center}
.service-icon{width:40px;height:36px;background:#222;border-radius:3px}
.service-name{margin-top:12px;font-size:13px;font-weight:700;color:#111;white-space:nowrap}

/* footer */
.site-footer{left:0;top:967px;width:884px;height:201px;background:var(--black)}
.foot-title{top:1000px;font-size:11.5px;font-weight:700;color:var(--white);letter-spacing:.3px}
.foot-title span{color:var(--blue)}
.foot-rule{top:1021px;width:25px}
.quick-links{left:73px;top:1034px;list-style:none;font-size:9.5px;color:var(--white)}
.quick-links li{height:24px}
.quick-links li::before{content:"• ";}
.quick-links .active{color:var(--blue)}
.contact-list{left:230px;top:1034px;width:170px;font-size:10px;color:var(--white);line-height:13.5px}
.contact-row{display:flex;gap:8px;margin-bottom:8px}
.contact-row svg{flex:none;margin-top:1px}
.map{left:460px;top:1037px;width:181px;height:94px;border:2px solid #888;background:linear-gradient(135deg,#e8e6dd,#d9d7cf 60%,#ece9de)}
.foot-brand{left:712px;top:1040px;width:96px;text-align:center;font-family:'Open Sans',sans-serif;font-weight:600;font-size:12px;line-height:16px;color:#bbb}
.social{left:712px;top:1114px;display:flex;gap:7px}
.social i{width:18px;height:18px;background:var(--blue)}
.copyright{left:0;top:1168px;width:884px;height:32px;background:var(--blue);color:var(--white);font-size:10px;display:flex;align-items:center;justify-content:center}
</style>
</head>
<body>

<header class="abs site-header">
  <div class="abs brand"><div class="brand-mark"></div><span class="brand-name">Marcus Delwyn-Hart Finance</span></div>
  <nav class="abs main-nav">
    <span class="active">HOME</span><span>ABOUT US</span><span>SERVICES</span><span>CONTACT US</span>
  </nav>
  <div class="abs call">
    <svg width="24" height="24" viewBox="0 0 24 24" fill="#2e5ca8"><path d="M6.6 10.8c1.4 2.8 3.8 5.1 6.6 6.6l2.2-2.2c.3-.3.7-.4 1-.2 1.1.4 2.3.6 3.6.6.6 0 1 .4 1 1V20c0 .6-.4 1-1 1C10.6 21 3 13.4 3 4c0-.6.4-1 1-1h3.5c.6 0 1 .4 1 1 0 1.3.2 2.5.6 3.6.1.3 0 .7-.2 1z"/></svg>
    <div class="call-divider"></div>
    <div class="call-text"><span>CALL US</span>(123)-555-0148</div>
  </div>
</header>

<section class="abs hero" role="img" aria-label="Two engineers in hard hats reviewing plans at a construction site with cranes under a cloudy sky"></section>
<div class="abs hero-caption"></div>
<h1 class="abs hero-title head-font">Construction Finance</h1>
<p class="abs hero-lead">Lorem ipsum dolor sit amet, consectetuer adipiscing elit, sed diam nonummy nib adipiscing elit, ed diam nonummy nibh euis</p>
<div class="abs btn hero-btn">CALL US TODAY</div>
<div class="abs dots"><i></i><i></i></div>

<h2 class="abs welcome-title head-font">WELCOME TO <span>MARCUS DELWYN-HART</span> FINANCE</h2>
<div class="abs rule welcome-rule"></div>
<p class="abs welcome-text">Lorem ipsum dolor sit amet, consectetuer adipiscing elit, sed diam nonummy nibh euismod tincidunt ut laoreet dolore magna aliquam erat volutpat. Ut wisi enim ad minim veniam, quis nostrud exerci tation ullamcorper suscipit lobortis nisl ut aliquip ex ea commodo consequat. Duis autem vel eum iriure dolor in hendrerit in vulputate velit esse molestie consequat, vel illum dolore eu feugiat nulla facilisis at vero eros et accumsan et iusto odio dignissim qui blandit praesent luptatum zzril delenit augue duis dolore te feugait nulla facilisi.</p>
<div class="abs btn read-btn">READ MORE</div>

<aside class="abs inquiry">
  <h3 class="abs inquiry-title head-font">QUICK <span>INQUIRY</span></h3>
  <div class="abs field" style="top:42px;height:28px">Name</div>
  <div class="abs field" style="top:75px;height:28px">Email</div>
  <div class="abs field" style="top:108px;height:52px">Message</div>
  <div class="abs btn submit">SUBMIT</div>
</aside>

<section class="abs services-band"></section>
<h2 class="abs services-title head-font">OUR SERVICES</h2>
<div class="abs rule services-rule"></div>
<div class="abs service" style="left:63px"><div class="service-box"><div class="service-icon" role="img" aria-label="Excavator icon"></div></div><div class="service-name">Equipment Finance</div></div>
<div class="abs service" style="left:219px"><div class="service-box"><div class="service-icon" role="img" aria-label="Hand holding money icon"></div></div><div class="service-name">Business Finance</div></div>
<div class="abs service" style="left:378px"><div class="service-box"><div class="service-icon" role="img" aria-label="Office building icon"></div></div><div class="service-name">Commercial Finance</div></div>
<div class="abs service" style="left:533px"><div class="service-box"><div class="service-icon" role="img" aria-label="Crane and building icon"></div></div><div class="service-name">Construction Finance</div></div>
<div class="abs service" style="left:689px"><div class="service-box"><div class="service-icon" role="img" aria-label="Bridge icon"></div></div><div class="service-name">Bridging Finance</div></div>

<footer class="abs site-footer"></footer>
<h4 class="abs foot-title head-font" style="left:73px">QUICK <span>LINKS</span></h4>
<div class="abs rule foot-rule" style="left:73px"></div>
<ul class="abs quick-links"><li class="active">HOME</li><li>ABOUT US</li><li>SERVICES</li><li>CONTACT US</li></ul>

<h4 class="abs foot-title head-font" style="left:230px">CONTACT <span>DETAILS</span></h4>
<div class="abs rule foot-rule" style="left:230px"></div>
<div class="abs contact-list">
  <div class="contact-row"><svg width="9" height="12" viewBox="0 0 9 12"><path d="M4.5 0A4.5 4.5 0 0 0 0 4.5C0 8 4.5 12 4.5 12S9 8 9 4.5A4.5 4.5 0 0 0 4.5 0zm0 6.3a1.8 1.8 0 1 1 0-3.6 1.8 1.8 0 0 1 0 3.6z" fill="#2e5ca8"/></svg><div><b>Marcus Delwyn-Hart Finance</b><br>Sed ut perspiciatis unde omnis iste natus errorluptatem</div></div>
  <div class="contact-row"><svg width="9" height="10" viewBox="0 0 24 24" fill="#2e5ca8"><path d="M6.6 10.8c1.4 2.8 3.8 5.1 6.6 6.6l2.2-2.2c.3-.3.7-.4 1-.2 1.1.4 2.3.6 3.6.6.6 0 1 .4 1 1V20c0 .6-.4 1-1 1C10.6 21 3 13.4 3 4c0-.6.4-1 1-1h3.5c.6 0 1 .4 1 1 0 1.3.2 2.5.6 3.6.1.3 0 .7-.2 1z"/></svg><div>0123 555 014</div></div>
  <div class="contact-row"><svg width="9" height="10" viewBox="0 0 10 8"><rect width="10" height="8" fill="#2e5ca8"/><path d="M0 0l5 4 5-4" stroke="#000" fill="none"/></svg><div>info@delwynhartfinance.com</div></div>
</div>

<h4 class="abs foot-title head-font" style="left:458px">LOCATION <span>MAP</span></h4>
<div class="abs rule foot-rule" style="left:458px"></div>
<div class="abs map" role="img" aria-label="Street map showing the office location"></div>

<div class="abs foot-brand">Marcus Delwyn-Hart Finance</div>
<div class="abs social"><i></i><i></i><i></i><i></i></div>

<div class="abs copyright">Copyright © 2017 Marcus Delwyn-Hart Finance. All Rights Reserved</div>

</body>
</html>
```